Bref créative
Business Cards and Stationary for Conference App Company
Kalvornet
Modern
Lars Henrik Dalsgaard
Partner
Solbærvej 254
DK-4100 Ringsted
lhd@kalvornet.example
kalvornet.example

```html
<!DOCTYPE html>
<html lang="en">
<head>
<meta charset="utf-8">
<title>Kalvornet – Business Card</title>
<link href="https://fonts.googleapis.com/css2?family=Open+Sans:ital,wght@0,300;0,400;0,600;1,400&display=swap" rel="stylesheet">
<style>
  :root {
    --stage: #e9eaeb;
    --card-white: #ffffff;
    --brand-grey: #8a8c8e;
    --band-grey: #9a9c9e;
    --text-grey: #6d6f71;
    --text-light: #9b9d9f;
    --rule-grey: #c9cacb;
    --brand-orange: #f5a01a;
    --orange-soft: #fbc15a;
  }
  * { margin: 0; padding: 0; box-sizing: border-box; }
  html, body {
    width: 1200px; height: 980px; overflow: hidden;
    background: var(--stage);
    font-family: "Open Sans", Arial, sans-serif;
  }
  .canvas { position: relative; width: 1200px; height: 980px; }
  .card {
    position: absolute; left: 210px;
    width: 780px; height: 440px;
    border-radius: 26px; overflow: hidden;
    box-shadow: 0 6px 18px rgba(0,0,0,0.12);
  }
  /* back side */
  .card--back { top: 40px; background: var(--brand-grey); }
  .back-brand {
    position: absolute; left: 90px; top: 120px;
    display: flex; align-items: center; gap: 26px;
  }
  .back-brand__dot {
    width: 110px; height: 110px; border-radius: 50%;
    background: var(--card-white);
  }
  .back-brand__name {
    font-size: 64px; font-weight: 300; color: var(--card-white);
    letter-spacing: 1px;
  }
  .back-url {
    position: absolute; right: 48px; bottom: 40px;
    font-size: 20px; letter-spacing: 5px; color: var(--card-white);
  }
  /* front side */
  .card--front { top: 500px; background: var(--card-white); }
  .front-band { position: absolute; inset: 0; }
  .front-logo {
    position: absolute; left: 150px; top: 56px;
    display: flex; align-items: center; gap: 14px;
  }
  .front-logo__dot {
    width: 44px; height: 44px; border-radius: 50%;
    background: var(--text-light);
  }
  .front-logo__name {
    font-size: 52px; font-weight: 300; color: var(--text-grey);
    line-height: 1;
  }
  .tagline {
    position: absolute; left: 210px; top: 116px;
    font-size: 22px; font-weight: 300; color: var(--text-light);
  }
  .person {
    position: absolute; left: 210px; top: 158px;
    width: 290px; text-align: right;
  }
  .person__name {
    font-size: 22px; font-weight: 600; color: var(--brand-orange);
  }
  .person__role {
    font-size: 16px; font-style: italic; color: var(--text-light);
  }
  .address {
    position: absolute; left: 70px; top: 246px; width: 200px;
    font-size: 15px; font-style: normal; line-height: 1.55;
    color: var(--text-grey); text-align: right;
  }
  .divider {
    position: absolute; left: 284px; top: 244px;
    width: 1px; height: 76px; background: var(--rule-grey);
  }
  .contact {
    position: absolute; left: 300px; top: 240px;
    list-style: none; font-size: 15px; color: var(--text-grey);
  }
  .contact li { display: flex; align-items: center; gap: 10px; height: 26px; }
  .contact svg { width: 18px; height: 18px; flex: none; }
</style>
</head>
<body>
<main class="canvas">

  <section class="card card--back" aria-label="Card back">
    <div class="back-brand">
      <span class="back-brand__dot"></span>
      <span class="back-brand__name">Kalvornet</span>
    </div>
    <p class="back-url">www.kalvornet.example</p>
  </section>

  <section class="card card--front" aria-label="Card front">
    <svg class="front-band" viewBox="0 0 780 440" preserveAspectRatio="none" aria-hidden="true">
      <path d="M0 300 C 220 330, 480 400, 780 330 L780 440 L0 440 Z" fill="var(--band-grey)"/>
      <path d="M0 290 C 240 318, 500 392, 780 318 L780 332 C 500 408, 240 338, 0 306 Z" fill="var(--brand-orange)"/>
      <path d="M520 0 C 600 60, 700 90, 780 96 L780 108 C 690 104, 590 72, 506 0 Z" fill="var(--orange-soft)"/>
    </svg>

    <div class="front-logo">
      <span class="front-logo__dot"></span>
      <span class="front-logo__name">Kalvornet</span>
    </div>
    <p class="tagline">Meetings Made Simple</p>

    <div class="person">
      <p class="person__name">Lars Henrik Dalsgaard</p>
      <p class="person__role">Partner</p>
    </div>

    <address class="address">
      Solbærvej 254<br>
      DK-4100 Ringsted
    </address>

    <span class="divider" aria-hidden="true"></span>

    <ul class="contact">
      <li>
        <svg viewBox="0 0 18 18" aria-hidden="true"><circle cx="9" cy="9" r="9" fill="var(--brand-orange)"/><path d="M6 5 l2 0 l1 2.5 l-1.2 1 a6 6 0 0 0 2.7 2.7 l1-1.2 l2.5 1 l0 2 a1 1 0 0 1-1 1 a8 8 0 0 1-8-8 a1 1 0 0 1 1-1z" fill="#fff"/></svg>
        +45 21098765
      </li>
      <li>
        <svg viewBox="0 0 18 18" aria-hidden="true"><circle cx="9" cy="9" r="9" fill="var(--brand-orange)"/><rect x="4.5" y="6" width="9" height="6.5" fill="#fff"/><path d="M4.5 6 L9 9.5 L13.5 6" stroke="var(--brand-orange)" fill="none"/></svg>
        lhd@kalvornet.example
      </li>
      <li>
        <svg viewBox="0 0 18 18" aria-hidden="true"><circle cx="9" cy="9" r="9" fill="var(--brand-orange)"/><circle cx="9" cy="9" r="4.5" stroke="#fff" fill="none"/><path d="M4.5 9 H13.5 M9 4.5 V13.5" stroke="#fff"/></svg>
        www.kalvornet.example
      </li>
    </ul>
  </section>

</main>
</body>
</html>
```